Table Tent Project for 50's Cafe

We need a graphic design which will be used on a table tent at a small 50's Cafe.

The restaurant is the Silver Spoke Cafe in Surrey, British Columbia, Canada.

Many photos can be found online at:
FriendWall: https://www.friendwall.example/thesilverspokecafe/
SnapGrid: https://www.snapgrid.example/silverspokecafe/

The purpose of this design is to create a table tent that informs customers about our social media presence.

Front: We would like it to include "Post a photo on SnapGrid, FriendWall or Chirper and get 10% off your meal!" on the front.

Back: We would love to hear from you! Please take the time to review us online!

Thank you!

Industry/Entity Type

Restaurant

Requirements
Must have
• Please include the three Social Media icons (FriendWall, SnapGrid, Chirper)
• Please keep the 50's theme.

```html
<!DOCTYPE html>
<html lang="en">
<head>
<meta charset="utf-8">
<title>Silver Spoke Cafe – Table Tent</title>
<link rel="stylesheet" href="https://fonts.googleapis.com/css2?family=Arimo:ital,wght@0,400;0,700;1,700&family=Kaushan+Script&family=Nunito:wght@900&family=Tinos&display=swap">
<style>
  :root{
    --teal:#3a9b9a;
    --teal-deep:#1f7677;
    --ink:#1c1c1c;
    --paper:#ffffff;
    --fold:#daeef5;
    --checker:#3a3a3a;
    --canvas:#ffffff;
  }
  *{box-sizing:border-box;margin:0;padding:0}
  html,body{width:1200px;height:1200px;overflow:hidden;background:var(--canvas)}
  .sheet{position:relative;width:1200px;height:1200px}

  /* fold-under tabs */
  .fold-tab{position:absolute;background:var(--fold);display:flex;align-items:center;
    font-family:"Tinos",serif;color:var(--ink)}
  .fold-tab--top{top:610px;height:250px;width:502px;font-size:14px;padding-left:157px}
  .fold-tab--left{left:206px;top:901px;width:129px;height:254px;justify-content:center}
  .fold-tab--right{left:893px;top:901px;width:132px;height:254px;justify-content:center}
  .fold-tab__note--turned{font-size:6px;white-space:nowrap}
  .fold-tab--left .fold-tab__note--turned{transform:rotate(90deg)}
  .fold-tab--right .fold-tab__note--turned{transform:rotate(-90deg)}

  /* panel artboard: 360 x 396 units */
  .panel{position:absolute;left:0;top:0;width:360px;height:396px;background:var(--paper);
    overflow:hidden;outline:1px solid #444;transform-origin:0 0;font-family:"Arimo",sans-serif;color:var(--ink)}
  .panel--back-large{transform:translate(50px,50px) scale(1.395)}
  .panel--front-large{transform:translate(653px,50px) scale(1.395)}
  .panel--back-small{transform:translate(614px,901px) rotate(90deg) scale(.705)}
  .panel--front-small{transform:translate(614px,1155px) rotate(-90deg) scale(.705)}

  .panel > *{position:absolute}
  .checker{background:var(--checker)}
  .photo{box-shadow:2px 3px 6px rgba(0,0,0,.45);border:5px solid #fff}
  .photo--breakfast{left:4px;top:14px;width:150px;height:120px;transform:rotate(-4deg);
    background:linear-gradient(135deg,#3f6fa8,#c8873b 55%,#f1d66b)}
  .photo--guests{left:0;top:140px;width:164px;height:134px;transform:rotate(-4deg);
    background:linear-gradient(160deg,#8a8f8a,#d07a3f 45%,#6b5040)}
  .photo--sign{left:150px;top:152px;width:210px;height:214px;
    background:linear-gradient(160deg,var(--teal) 0%,var(--teal-deep) 60%,#2a6a6a)}
  .photo--sign-small{left:232px;top:0;width:128px;height:66px;
    background:linear-gradient(180deg,#6a8fb8,#3f6c82)}
  .photo--reader{left:140px;top:170px;width:220px;height:226px;
    clip-path:polygon(9% 0,100% 0,100% 100%,0 100%);
    background:linear-gradient(135deg,#b9c8cf,#2b3548 55%,#171a24)}

  .headline{font-family:"Nunito",sans-serif;font-weight:900;color:var(--teal);line-height:1}
  .script{font-family:"Kaushan Script",cursive;color:var(--teal);line-height:1}

  .back__save{left:175px;width:185px;top:26px;text-align:center;font-size:23px}
  .back__by{left:175px;width:185px;top:53px;text-align:center;font-size:15px}
  .back__photos{left:168px;width:192px;top:73px;text-align:center;font-size:43px;letter-spacing:.5px}
  .back__of{left:175px;width:185px;top:118px;text-align:center;font-size:10px}
  .back__tell{left:168px;width:192px;top:130px;text-align:center;font-size:10px}
  .back__tell em{font-family:"Kaushan Script",cursive;font-style:normal}
  .back__rule{left:150px;top:151px;width:210px;height:1px;background:var(--ink)}
  .back__review{left:8px;top:314px;width:136px;font-size:9.5px;line-height:1.45}
  .back__review em{font-family:"Kaushan Script",cursive;font-style:normal;font-size:10px}

  .social{display:flex;gap:4px}
  .social__item{display:flex;align-items:center;gap:2px;font-family:"Arimo",sans-serif;
    font-weight:700;font-size:7px;color:var(--ink);white-space:nowrap}
  .social__mark{width:8px;height:8px;background:var(--teal)}
  .social--back{left:8px;top:374px}
  .social--front{left:8px;top:374px}
  .social--front .social__item{color:#fff}
  .social--front .social__mark{background:#fff}

  .front__post{left:0;width:232px;top:18px;text-align:center;font-size:10.5px;line-height:1.35}
  .front__post b{font-style:italic}
  .front__off{left:0;width:340px;top:74px;text-align:center;font-size:56px;letter-spacing:1px}
  .front__meal{left:80px;width:280px;top:126px;text-align:center;font-size:30px}
  .front__band{left:0;top:188px;width:150px;height:38px;transform:skewY(2deg)}
  .front__box{left:0;top:226px;width:146px;height:170px;background:var(--teal);
    clip-path:polygon(0 0,100% 0,96% 100%,0 100%)}
  .front__upload{left:14px;width:116px;top:238px;text-align:center;font-size:14px;line-height:1.2;color:#fff}
  .front__like{left:12px;width:120px;top:302px;text-align:center;font-size:7.5px;line-height:1.4;color:#fff}
</style>
</head>
<body>
<main class="sheet">

  <!-- back panel, flat -->
  <section class="panel panel--back-large" aria-label="Back of table tent">
    <div class="checker" style="left:0;top:0;width:360px;height:14px" role="img" aria-label="Black and white checkerboard strip"></div>
    <div class="photo photo--breakfast" role="img" aria-label="Photo of a breakfast plate"></div>
    <div class="photo photo--guests" role="img" aria-label="Photo of guests at a diner table"></div>
    <div class="photo--sign" role="img" aria-label="Photo of the cafe's neon sign"></div>
    <p class="headline back__save">Save 10%</p>
    <p class="script back__by">by just uploading your</p>
    <p class="headline back__photos">PHOTOS</p>
    <p class="back__of">of the Silver Spoke Cafe</p>
    <p class="back__tell">and <em>tell us about your experience!</em></p>
    <div class="back__rule"></div>
    <p class="back__review">We would love to hear from you! <em>Please take time to review us online!</em></p>
    <div class="checker" style="left:160px;top:366px;width:200px;height:30px" role="img" aria-label="Black and white checkerboard strip"></div>
    <div class="social social--back">
      <span class="social__item"><span class="social__mark"></span>SnapGrid</span>
      <span class="social__item"><span class="social__mark"></span>FriendWall</span>
      <span class="social__item"><span class="social__mark"></span>Chirper</span>
    </div>
  </section>

  <!-- front panel, flat -->
  <section class="panel panel--front-large" aria-label="Front of table tent">
    <div class="checker" style="left:0;top:0;width:232px;height:14px" role="img" aria-label="Black and white checkerboard strip"></div>
    <div class="photo--sign-small" role="img" aria-label="Photo of the cafe sign against the sky"></div>
    <p class="front__post">Post a photo of your you, friends and family at Silver Spoke Cafe on our <b>FriendWall</b>, <b>SnapGrid</b> or <b>Chirper</b> and receive</p>
    <p class="headline front__off">10% OFF</p>
    <p class="script front__meal">Your Next Meal</p>
    <div class="photo--reader" role="img" aria-label="Photo of a guest reading the menu"></div>
    <div class="checker front__band" role="img" aria-label="Black and white checkerboard strip"></div>
    <div class="front__box"></div>
    <p class="script front__upload">Upload your photos of the Silver Spoke Cafe!</p>
    <p class="front__like">Don't forget to like our page for other special offers and future promotions!</p>
    <div class="social social--front">
      <span class="social__item"><span class="social__mark"></span>SnapGrid</span>
      <span class="social__item"><span class="social__mark"></span>FriendWall</span>
      <span class="social__item"><span class="social__mark"></span>Chirper</span>
    </div>
  </section>

  <div class="fold-tab fold-tab--top" style="left:50px">Folds under to sit on table</div>
  <div class="fold-tab fold-tab--top" style="left:653px">Folds under to sit on table</div>

  <!-- assembled tent preview -->
  <div class="fold-tab fold-tab--left"><span class="fold-tab__note--turned">Folds under to sit on table</span></div>
  <div class="fold-tab fold-tab--right"><span class="fold-tab__note--turned">Folds under to sit on table</span></div>

  <section class="panel panel--back-small" aria-label="Back of table tent, assembled view">
    <div class="checker" style="left:0;top:0;width:360px;height:14px" role="img" aria-label="Black and white checkerboard strip"></div>
    <div class="photo photo--breakfast" role="img" aria-label="Photo of a breakfast plate"></div>
    <div class="photo photo--guests" role="img" aria-label="Photo of guests at a diner table"></div>
    <div class="photo--sign" role="img" aria-label="Photo of the cafe's neon sign"></div>
    <p class="headline back__save">Save 10%</p>
    <p class="script back__by">by just uploading your</p>
    <p class="headline back__photos">PHOTOS</p>
    <p class="back__of">of the Silver Spoke Cafe</p>
    <p class="back__tell">and <em>tell us about your experience!</em></p>
    <div class="back__rule"></div>
    <p class="back__review">We would love to hear from you! <em>Please take time to review us online!</em></p>
    <div class="checker" style="left:160px;top:366px;width:200px;height:30px" role="img" aria-label="Black and white checkerboard strip"></div>
    <div class="social social--back">
      <span class="social__item"><span class="social__mark"></span>SnapGrid</span>
      <span class="social__item"><span class="social__mark"></span>FriendWall</span>
      <span class="social__item"><span class="social__mark"></span>Chirper</span>
    </div>
  </section>

  <section class="panel panel--front-small" aria-label="Front of table tent, assembled view">
    <div class="checker" style="left:0;top:0;width:232px;height:14px" role="img" aria-label="Black and white checkerboard strip"></div>
    <div class="photo--sign-small" role="img" aria-label="Photo of the cafe sign against the sky"></div>
    <p class="front__post">Post a photo of your you, friends and family at Silver Spoke Cafe on our <b>FriendWall</b>, <b>SnapGrid</b> or <b>Chirper</b> and receive</p>
    <p class="headline front__off">10% OFF</p>
    <p class="script front__meal">Your Next Meal</p>
    <div class="photo--reader" role="img" aria-label="Photo of a guest reading the menu"></div>
    <div class="checker front__band" role="img" aria-label="Black and white checkerboard strip"></div>
    <div class="front__box"></div>
    <p class="script front__upload">Upload your photos of the Silver Spoke Cafe!</p>
    <p class="front__like">Don't forget to like our page for other special offers and future promotions!</p>
    <div class="social social--front">
      <span class="social__item"><span class="social__mark"></span>SnapGrid</span>
      <span class="social__item"><span class="social__mark"></span>FriendWall</span>
      <span class="social__item"><span class="social__mark"></span>Chirper</span>
    </div>
  </section>

</main>
</body>
</html>
```